Super elegant, crisp & clean Business card design required

We recently upgraded our branding - which is on our website - tavorelstudio.com

I would like a simple, yet elegant, clean business card design please.

The font of my logo is Cinzel - and because of the natural colour - it's best to have this on a black background.

I would like to have the back of the business card - with simply my logo.

PLEASE DO NOT SUBMIT A COMPLICATED / UNCLEAN DESIGN

Industry/Entity Type

Business

Contact Information for Business Card

Dalvik Ostrander Photography

Font styles to use
Other font styles liked:
• Cinzel

Requirements
Must have
• A backpage with nothing but my logo
• Simple design - stands out
Should not have
• Colour that dont align with my logo
• Over complicated '/ non symmetrical design

```html
<!DOCTYPE html>
<html lang="en">
<head>
<meta charset="utf-8">
<title>Dalvik Ostrander Photography – Business Card</title>
<link rel="stylesheet" href="https://fonts.googleapis.com/css2?family=Cinzel:wght@400;600&display=swap">
<style>
  :root {
    --backdrop: #2f2f2f;
    --card-light: #ffffff;
    --card-light-edge: #e4e4e4;
    --card-dark: #151515;
    --card-dark-edge: #0d0d0d;
    --brand-brown: #7a6a55;
    --text-grey: #6e6e6e;
    --brand-white: #f4f4f4;
  }
  * { margin: 0; padding: 0; box-sizing: border-box; }
  html, body {
    width: 1200px; height: 965px; overflow: hidden;
    background: var(--backdrop);
    font-family: "Cinzel", serif;
  }
  .canvas { position: relative; width: 1200px; height: 965px; }

  .card {
    position: absolute; left: 246px; width: 710px; height: 402px;
    box-shadow: 0 3px 8px rgba(0,0,0,0.45);
  }
  .card--front {
    top: 60px;
    background: radial-gradient(ellipse at 60% 40%, var(--card-light) 35%, var(--card-light-edge) 100%);
  }
  .card--back {
    top: 505px;
    background: radial-gradient(ellipse at 50% 50%, var(--card-dark) 40%, var(--card-dark-edge) 100%);
  }

  .wordmark { position: absolute; text-align: center; line-height: 1; font-weight: 400; }
  .wordmark__name { display: block; font-size: 21px; letter-spacing: 0.01em; }
  .wordmark__trade { display: block; font-size: 10.5px; letter-spacing: 0.5em; margin-top: 3px; padding-left: 0.5em; }

  .card--front .wordmark { left: 49px; top: 162px; width: 242px; color: var(--brand-brown); }
  .card--back .wordmark { left: 0; width: 710px; top: 245px; color: var(--brand-white); }

  .holder {
    position: absolute; right: 51px; top: 216px; text-align: right; line-height: 1;
  }
  .holder__name { font-size: 22px; font-weight: 600; color: var(--brand-brown); }
  .holder__role { font-size: 16px; color: var(--text-grey); margin-top: 4px; }

  .contacts { position: absolute; left: 50px; top: 301px; list-style: none; }
  .contacts__item {
    display: flex; align-items: center; height: 21px;
    font-size: 15px; color: var(--text-grey); letter-spacing: 0.01em;
  }
  .contacts__icon { width: 14px; height: 14px; margin-right: 12px; fill: var(--text-grey); }
</style>
</head>
<body>
<main class="canvas">
  <section class="card card--front" aria-label="Card front">
    <div class="wordmark">
      <span class="wordmark__name">Dalvik Ostrander</span>
      <span class="wordmark__trade">Photography</span>
    </div>

    <div class="holder">
      <p class="holder__name">Dalvik Ostrander</p>
      <p class="holder__role">Photographer</p>
    </div>

    <ul class="contacts">
      <li class="contacts__item">
        <svg class="contacts__icon" viewBox="0 0 24 24" aria-hidden="true"><path d="M6.6 10.8a15.1 15.1 0 0 0 6.6 6.6l2.2-2.2c.3-.3.7-.4 1-.2 1.1.4 2.3.6 3.6.6.6 0 1 .4 1 1V20c0 .6-.4 1-1 1A17 17 0 0 1 3 4c0-.6.4-1 1-1h3.5c.6 0 1 .4 1 1 0 1.3.2 2.5.6 3.6.1.3 0 .7-.2 1z"/></svg>
        07 700 900 412
      </li>
      <li class="contacts__item">
        <svg class="contacts__icon" viewBox="0 0 24 24" aria-hidden="true"><path d="M2 5h20v14H2zm2 2v.5l8 5 8-5V7zm0 2.8V17h16V9.8l-8 5z"/></svg>
        info@tavorelstudio.com
      </li>
      <li class="contacts__item">
        <svg class="contacts__icon" viewBox="0 0 24 24" aria-hidden="true"><path d="M12 2a10 10 0 1 0 0 20 10 10 0 0 0 0-20zm6.9 6h-3a15 15 0 0 0-1.3-3.9A8 8 0 0 1 18.9 8zM12 4c.8 1.2 1.5 2.5 1.9 4h-3.8c.4-1.5 1.1-2.8 1.9-4zM4.3 14a8 8 0 0 1 0-4h3.4a16 16 0 0 0 0 4zm.8 2h3a15 15 0 0 0 1.3 3.9A8 8 0 0 1 5.1 16zm3-8h-3a8 8 0 0 1 4.3-3.9A15 15 0 0 0 8.1 8zM12 20c-.8-1.2-1.5-2.5-1.9-4h3.8c-.4 1.5-1.1 2.8-1.9 4zm2.3-6H9.7a14 14 0 0 1 0-4h4.6a14 14 0 0 1 0 4zm.3 5.9a15 15 0 0 0 1.3-3.9h3a8 8 0 0 1-4.3 3.9zm1.7-5.9a16 16 0 0 0 0-4h3.4a8 8 0 0 1 0 4z"/></svg>
        www.tavorelstudio.com
      </li>
    </ul>
  </section>

  <section class="card card--back" aria-label="Card back">
    <div class="wordmark">
      <span class="wordmark__name">Dalvik Ostrander</span>
      <span class="wordmark__trade">Photography</span>
    </div>
  </section>
</main>
</body>
</html>
```